Bramwell Exteriors Needs a New Website!

We are an exteriors company specializing in vinyl siding, Peter Aldous siding, aluminum soffit/fascia, trough. We do new construction work as well as renovations. We also build detached garages.
You can view our current website at www.bramwellbuilders.ca
I want to completely overhaul the website.
Our services are different now as we no longer do new home construction as well as we do not do the snow clearing.
I want to focus on 2 things in particular on the website:

1/ Exterior renovations

2/ Detached Garage construction.

I have included our logo in the attached files to use as well.

Some features we would like:

1/ Be able to easily attach a video from Youtube/Vimeo to highlight a product or service
2/ Quick chat or contact button that we can talk to a potential client quickly
3/ Meet the Team page that is interesting and fresh
4/ Place for us to put in helpful exterior tips/suggestions for homeowners.

Content is not important, but looking for the best design that will attract people once they click on our page and want to renovate with us.

Target Market(s)

People looking for renovations on their home, people looking to build a detached garage.

Industry/Entity Type

Residential Construction

Coding

Coded - Design and coding required

Number of Pages Required

5+ page

Font styles to use
Sans Serif

Requirements
Must have
• Fresh and exciting home page.

Simple design. Don't want it over complicated or too much information to confuse the potential client.

Easy way to contact us.

Meet the team page that instills confidence
Nice to have
• Colour of website to go off our logo. Doesn't need to be an exact match, but something that goes well with our blue and grey.

```html
<!DOCTYPE html>
<html lang="en">
<head>
<meta charset="utf-8">
<title>Bramwell Exteriors</title>
<link href="https://fonts.googleapis.com/css2?family=Montserrat:wght@500;600;700;800&family=Open+Sans:wght@400;600;700&display=swap" rel="stylesheet">
<style>
:root{
  --green:#2db36a;
  --dark:#2b2b2b;
  --ink:#222;
  --muted:#9a9a9a;
  --frame:#bdbdbd;
  --line:#d6d6d6;
  --white:#fff;
}
*{margin:0;padding:0;box-sizing:border-box}
html,body{width:1200px;height:3597px;overflow:hidden;background:var(--white)}
body{position:relative;font-family:"Open Sans",sans-serif;color:var(--ink)}
.abs{position:absolute}
.page{position:absolute;left:155px;top:169px;width:889px;height:3256px;background:var(--white);box-shadow:0 0 40px rgba(0,0,0,.08)}
.heading{font-family:"Montserrat",sans-serif;font-weight:700;color:var(--ink)}
.body-text{font-size:11px;line-height:15.5px;color:var(--muted)}
/* nav */
.nav{left:155px;top:169px;width:889px;height:53px;background:var(--white)}
.brand{left:223px;top:178px;display:flex;align-items:center;gap:8px;font-family:"Montserrat",sans-serif;font-weight:700;font-size:17px;color:#1f4f8a}
.brand-dot{width:34px;height:34px;border-radius:50%;background:#1f4f8a}
.nav-link{top:169px;height:53px;line-height:53px;font-size:11px;color:#8a8a8a;text-align:center}
.nav-link.active{background:var(--dark);color:var(--white);font-weight:600}
/* hero */
.hero{left:155px;top:222px;width:889px;height:423px;background:linear-gradient(180deg,#5a5a74 0%,#3c4660 45%,#2e3447 75%,#4a4a52 100%)}
.hero-eyebrow{left:246px;top:286px;font-size:12px;color:#e8e8e8}
.hero-bar{left:244px;top:314px;width:4px;height:92px;background:var(--white)}
.hero-title{left:263px;top:316px;font-family:"Montserrat",sans-serif;font-weight:800;font-size:30px;line-height:43px;color:var(--white);white-space:nowrap}
.hero-text{left:246px;top:418px;width:230px;font-size:12px;line-height:17px;color:#eee}
.btn-dark{background:var(--dark);color:var(--white);font-size:9.5px;font-weight:700;border-radius:14px;text-align:center}
/* labels */
.tag{height:25px;line-height:25px;background:var(--green);color:var(--white);font-size:10.5px;text-align:center}
.tag-rule{left:155px;height:3px;width:84px;background:var(--green)}
/* photos */
.photo{position:absolute}
.frame{position:absolute;border:7px solid var(--frame)}
.num{font-family:"Montserrat",sans-serif;font-weight:700;font-size:17px}
.feature-title{font-family:"Montserrat",sans-serif;font-weight:700;font-size:21.5px;line-height:34px;white-space:nowrap}
.accent{height:4px;width:62px;background:var(--green)}
/* news */
.news-grid{left:420px;top:2232px;width:558px;height:215px;display:flex;border:1px solid #c9c9c9}
.news-card{flex:1;border-right:1px solid #c9c9c9;padding:26px 8px 0 21px;position:relative}
.news-card:last-child{border-right:none}
.news-title{font-family:"Montserrat",sans-serif;font-weight:500;font-size:13.5px;line-height:21px;white-space:nowrap}
.news-date{font-size:8px;color:#777;margin-top:12px}
.news-text{font-size:8px;line-height:12.5px;color:var(--muted);margin-top:9px;width:120px}
.news-rule{height:1px;background:#ccc;margin-top:12px;margin-right:10px}
.btn-green{display:inline-block;width:71px;height:26px;line-height:26px;border-radius:14px;background:var(--green);color:var(--white);font-size:9.5px;font-weight:600;text-align:center;margin-top:13px}
/* stats */
.stats{left:155px;top:2532px;width:889px;height:286px;background:linear-gradient(135deg,#3a3a34 0%,#1f211e 50%,#2c2e2a 100%)}
.stats-frame{left:278px;top:2590px;width:110px;height:170px;border:5px solid #8d8d8d}
.stats-title{left:213px;top:2614px;font-family:"Montserrat",sans-serif;font-weight:600;font-size:20px;line-height:30.5px;color:var(--white);white-space:nowrap}
.stats-text{left:550px;top:2618px;width:410px;font-size:9.5px;line-height:13px;color:#ddd}
.stat{top:2680px;color:var(--white);text-align:center}
.stat-num{font-family:"Montserrat",sans-serif;font-weight:500;font-size:42px;line-height:50px}
.stat-label{font-size:8.5px;font-weight:600;margin-top:6px}
/* pricing */
.price-card{top:2872px;width:160px;height:294px;border:4px solid var(--frame);text-align:center;background:var(--white)}
.price-card.featured{border-color:var(--green)}
.price-name{font-family:"Montserrat",sans-serif;font-weight:500;font-size:15px;line-height:21px;margin-top:23px}
.price-amount{font-size:12px;color:#666;margin-top:8px}
.price-row{margin:0 auto;width:104px;border-bottom:1px solid var(--line);font-size:11px;color:#666;padding:4px 0 5px}
.price-rows{margin-top:18px}
.price-rule{width:120px;height:1px;background:var(--line);margin:18px auto 0}
.btn-outline{display:inline-block;width:76px;height:27px;line-height:23px;border:2px solid var(--green);border-radius:14px;color:var(--green);font-size:9px;margin-top:18px}
.btn-solid{display:inline-block;width:76px;height:27px;line-height:27px;background:var(--green);border-radius:14px;color:var(--white);font-size:9px;font-weight:600;margin-top:18px}
.badge{position:absolute;left:50%;top:-4px;transform:translateX(-50%);background:var(--green);color:var(--white);font-size:5px;padding:2px 7px;font-weight:700}
/* footer */
.footer{left:155px;top:3234px;width:889px;height:191px;background:var(--dark);color:var(--white)}
.foot-brand{left:250px;top:3268px;font-family:"Montserrat",sans-serif;font-weight:800;font-size:28px;color:var(--white)}
.foot-text{left:250px;top:3318px;width:210px;font-size:8.5px;line-height:12px;color:#ddd}
.foot-copy{left:250px;top:3362px;font-size:8.5px;color:#ddd}
.foot-col{top:3271px;font-size:9px;line-height:18px;color:var(--white)}
.foot-col h4{font-size:9px;font-weight:600;margin-bottom:14px}
.search{left:878px;top:3301px;width:106px;height:25px;background:#6c6c6c;color:#eee;font-size:9px;line-height:25px;padding-left:10px}
</style>
</head>
<body>
<div class="page"></div>

<!-- navigation -->
<header class="abs nav"></header>
<div class="abs brand"><span class="brand-dot"></span>Bramwell Exteriors</div>
<a class="abs nav-link active" style="left:512px;width:108px">HOME</a>
<a class="abs nav-link" style="left:620px;width:80px">PROJECTS</a>
<a class="abs nav-link" style="left:715px;width:80px">ABOUT</a>
<a class="abs nav-link" style="left:809px;width:80px">SERVICES</a>
<a class="abs nav-link" style="left:908px;width:80px">CONTACT</a>

<!-- hero -->
<section class="abs hero" role="img" aria-label="Two-storey family home with double garage at dusk"></section>
<p class="abs hero-eyebrow">Exteriors Company</p>
<div class="abs hero-bar"></div>
<h1 class="abs hero-title">EXPERIENCE THE<br>BRAMWELL DIFFERENCE</h1>
<p class="abs hero-text">Lorem ipsum dolor sit amet, consectetur adipiscing elit. Cras lacinia magna vel molestie faucibus.</p>
<a class="abs btn-dark" style="left:247px;top:497px;width:70px;height:22px;line-height:22px">Read More</a>

<!-- about -->
<div class="abs tag-rule" style="top:725px"></div>
<div class="abs tag" style="left:239px;top:703px;width:82px">About Us</div>
<h2 class="abs heading" style="left:239px;top:744px;font-size:20px;line-height:30.5px;white-space:nowrap">Welcome ! We are BRAMWELL<br>Professional Exteriors<br>Company</h2>
<p class="abs body-text" style="left:239px;top:853px;width:330px">Lorem ipsum dolor sit amet, consectetur adipiscing elit. Cras lacinia magna vel molestie faucibus. Donec auctor et urnaLorem ipsum dolor sit amet, consectetur adipiscing elit. Cras lacinia magna vel molestie faucibus. Cras lacinia magna vel molestie faucibus. Donec auctor et urnaLorem ipsum dolor sit amet, consectetur adipiscing elit. Cras lacinia magna vel molestie faucibus.</p>
<p class="abs body-text" style="left:239px;top:976px;width:330px">Lorem ipsum dolor sit amet, consectetur adipiscing elit. Cras lacinia magna vel molestie faucibus. Donec auctor et urnaLorem ipsum dolor sit amet, consectetur adipiscing elit.</p>
<a class="abs btn-dark" style="left:239px;top:1044px;width:70px;height:26px;line-height:26px">Read More</a>
<div class="frame" style="left:656px;top:760px;width:297px;height:398px"></div>
<div class="photo" style="left:680px;top:731px;width:294px;height:398px;background:linear-gradient(180deg,#d9d9db 0%,#bdb8b2 45%,#8e8c8c 70%,#c9c8c6 100%)" role="img" aria-label="Bright kitchen with grey island and pendant lights"></div>

<!-- feature 1 -->
<div class="frame" style="left:253px;top:1252px;width:424px;height:256px"></div>
<div class="photo" style="left:233px;top:1229px;width:423px;height:257px;background:linear-gradient(180deg,#c8cdd3 0%,#5d6166 40%,#3b3e42 75%,#9fa2a5 100%)" role="img" aria-label="Dark-sided new home with stone accents in winter snow"></div>
<p class="abs num" style="left:745px;top:1224px">01</p>
<h3 class="abs feature-title" style="left:745px;top:1259px">Unrivalled Quality and<br>Attention to Detail</h3>
<div class="abs accent" style="left:745px;top:1334px"></div>
<p class="abs body-text" style="left:745px;top:1348px;width:222px">Lorem ipsum dolor sit amet, consectetur adipiscing elit. Cras lacinia magna vel molestie faucibus. Donec auctor et urnaLorem ipsum dolor sit amet, consectetur adipiscing elit.</p>

<!-- feature 2 -->
<p class="abs num" style="left:233px;top:1581px">02</p>
<h3 class="abs feature-title" style="left:233px;top:1616px">Current Custom Home<br>Build</h3>
<div class="abs accent" style="left:233px;top:1691px"></div>
<p class="abs body-text" style="left:233px;top:1705px;width:222px">Lorem ipsum dolor sit amet, consectetur adipiscing elit. Cras lacinia magna vel molestie faucibus. Donec auctor et urnaLorem ipsum dolor sit amet, consectetur adipiscing elit.</p>
<div class="frame" style="left:583px;top:1599px;width:360px;height:215px"></div>
<div class="photo" style="left:608px;top:1578px;width:359px;height:215px;background:linear-gradient(180deg,#b8babc 0%,#8d8f90 40%,#4a4947 70%,#6d655c 100%)" role="img" aria-label="Custom home under construction with siding in progress"></div>

<!-- feature 3 -->
<div class="frame" style="left:258px;top:1906px;width:419px;height:257px"></div>
<div class="photo" style="left:233px;top:1881px;width:420px;height:257px;background:linear-gradient(180deg,#2e3f6a 0%,#7a7688 35%,#8a6a45 60%,#2f4a22 85%,#1f3318 100%)" role="img" aria-label="Modern award-winning home lit at sunset over a lawn"></div>
<p class="abs num" style="left:745px;top:1881px">03</p>
<h3 class="abs feature-title" style="left:745px;top:1915px">Awards Winning<br>Exteriors</h3>
<div class="abs accent" style="left:745px;top:1990px"></div>
<p class="abs body-text" style="left:745px;top:2004px;width:222px">Lorem ipsum dolor sit amet, consectetur adipiscing elit. Cras lacinia magna vel molestie faucibus. Donec auctor et urnaLorem ipsum dolor sit amet, consectetur adipiscing elit.</p>

<!-- news -->
<div class="abs tag-rule" style="top:2256px"></div>
<div class="abs tag" style="left:239px;top:2235px;width:103px">LATEST NEWS</div>
<h2 class="abs heading" style="left:239px;top:2278px;font-size:18px;line-height:25.5px;width:140px">Fresh updates for you, read with detail.</h2>
<div class="abs news-grid">
  <article class="news-card">
    <h4 class="news-title">Plant Trees While<br>Searching The Web</h4>
    <p class="news-date">Jun 02, 2020</p>
    <p class="news-text">Lorem ipsum dolor sit amet, consectetur adipiscing elit. Cras lacinia magna vel molestie faucibus.</p>
    <div class="news-rule"></div>
    <a class="btn-green">Read More</a>
  </article>
  <article class="news-card">
    <h4 class="news-title">Plant Trees While<br>Searching The Web</h4>
    <p class="news-date">Jun 02, 2020</p>
    <p class="news-text">Lorem ipsum dolor sit amet, consectetur adipiscing elit. Cras lacinia magna vel molestie faucibus.</p>
    <div class="news-rule"></div>
    <a class="btn-green">Read More</a>
  </article>
  <article class="news-card">
    <h4 class="news-title">Plant Trees While<br>Searching The Web</h4>
    <p class="news-date">Jun 02, 2020</p>
    <p class="news-text">Lorem ipsum dolor sit amet, consectetur adipiscing elit. Cras lacinia magna vel molestie faucibus.</p>
    <div class="news-rule"></div>
    <a class="btn-green">Read More</a>
  </article>
</div>

<!-- stats -->
<section class="abs stats" role="img" aria-label="Modern home exterior at night, darkened background"></section>
<div class="abs stats-frame"></div>
<h2 class="abs stats-title">We are BRAMWELL<br>Professional<br>Exteriors<br>Company</h2>
<p class="abs stats-text">Lorem ipsum dolor sit amet, consectetur adipiscing elit. Cras lacinia magna vel molestie faucibus. Donec auctor et urnaLorem ipsum dolor sit amet, consectetur adipiscing elit. Cras lacinia magna vel molestie faucibus.</p>
<div class="abs stat" style="left:548px"><div class="stat-num">150+</div><div class="stat-label">HAPPY CUSTOMERS</div></div>
<div class="abs stat" style="left:681px"><div class="stat-num">320+</div><div class="stat-label">FINISHED PROJECTS</div></div>
<div class="abs stat" style="left:813px"><div class="stat-num">540+</div><div class="stat-label">DAYS OF WORKS</div></div>

<!-- pricing -->
<div class="abs tag-rule" style="top:2882px"></div>
<div class="abs tag" style="left:239px;top:2860px;width:103px">SPECIAL PRICES</div>
<h2 class="abs heading" style="left:239px;top:2914px;font-size:18px">Our Pricing List</h2>
<p class="abs body-text" style="left:239px;top:2950px;width:170px;font-size:8.5px;line-height:12.5px">Lorem ipsum dolor sit amet, consectetur adipiscing elit. Cras lacinia magna vel molestie faucibus. Donec auctor et urnaLorem ipsum dolor sit amet, consectetur adipiscing elit. Cras lacinia magna vel molestie faucibus.</p>

<div class="abs price-card" style="left:449px">
  <h4 class="price-name">Exterior<br>Renovations</h4>
  <p class="price-amount">$39,000</p>
  <div class="price-rows"><div class="price-row">77</div><div class="price-row">30</div><div class="price-row">x</div><div class="price-row">15</div></div>
  <div class="price-rule"></div>
  <a class="btn-outline">CONTACT US</a>
</div>
<div class="abs price-card featured" style="left:622px">
  <span class="badge">BEST VALUE</span>
  <h4 class="price-name">Exterior<br>Renovations</h4>
  <p class="price-amount">$39,000</p>
  <div class="price-rows"><div class="price-row">77</div><div class="price-row">30</div><div class="price-row">x</div><div class="price-row">15</div></div>
  <div class="price-rule"></div>
  <a class="btn-solid">CONTACT US</a>
</div>
<div class="abs price-card" style="left:796px">
  <h4 class="price-name">Exterior<br>Renovations</h4>
  <p class="price-amount">$39,000</p>
  <div class="price-rows"><div class="price-row">77</div><div class="price-row">30</div><div class="price-row">x</div><div class="price-row">15</div></div>
  <div class="price-rule"></div>
  <a class="btn-outline">CONTACT US</a>
</div>

<!-- footer -->
<footer class="abs footer"></footer>
<div class="abs foot-brand">BRAMWELL</div>
<p class="abs foot-text">Lorem ipsum dolor sit amet, consectetur adipiscing elit. Cras lacinia magna vel molestie faucibus.</p>
<p class="abs foot-copy">© Copyright 2020 BRAMWELL. All Rights reserved</p>
<div class="abs foot-col" style="left:501px"><h4>Site Map</h4>Home<br>About<br>Services<br>Contact</div>
<div class="abs foot-col" style="left:625px"><h4>Contact Us</h4>Call Us<br>555-014-2237<br>Mail Us<br>info@bramwellbuilders.ca</div>
<div class="abs foot-col" style="left:751px;line-height:13px"><h4 style="margin-bottom:19px">Visit Us</h4>Our Location<br>Cedarvale Park,<br>Alberta</div>
<div class="abs foot-col" style="left:878px"><h4>Search, Social Links</h4></div>
<div class="abs search">Search ...</div>
</body>
</html>
```